Income Tax Business Cards - Updates

Need to update these business cards while keeping all the same wording but just update them and make them look nicer and more modern/ on brand with our brand.

Industry/Entity Type

finance

Contact Information for Business Card

we have multiple locations so will just need to easily be able to change the address and phone numbers

Colors

Designer to choose colors to be used in the design.

```html
<!DOCTYPE html>
<html lang="en">
<head>
<meta charset="utf-8">
<title>Ledgerline Financial Group – Tax Season Business Card</title>
<link href="https://fonts.googleapis.com/css2?family=Source+Sans+3:wght@400;600;700&display=swap" rel="stylesheet">
<style>
  :root {
    --backdrop: #b3b3b3;
    --paper: #ffffff;
    --brand-green: #05502c;
    --brand-red: #c01f26;
    --ink-gray: #58595b;
  }
  * { margin: 0; padding: 0; box-sizing: border-box; }
  html, body {
    width: 1200px; height: 1200px; overflow: hidden;
    background: var(--backdrop);
    font-family: "Source Sans 3", "Myriad Pro", Arial, sans-serif;
  }
  .card {
    position: absolute; left: 276px; width: 648px; height: 370px;
    background: var(--paper); overflow: hidden;
  }
  .card--front { top: 197px; }
  .card--back { top: 633px; }
  .card__swoosh { position: absolute; inset: 0; width: 100%; height: 100%; }

  .brand-name {
    position: absolute; left: 28px; top: 52px;
    color: var(--brand-green); font-weight: 600; line-height: 1;
  }
  .brand-name__main { display: block; font-size: 40px; letter-spacing: -0.5px; }
  .brand-name__sub { display: block; font-size: 11px; letter-spacing: 3.6px; text-transform: uppercase; margin-top: 6px; padding-left: 2px; }

  .offer { position: absolute; right: 33px; text-align: right; line-height: 1; }
  .offer__amount { top: 44px; color: var(--brand-green); font-weight: 700; font-size: 25px; }
  .offer__amount span { display: block; margin-bottom: 1px; }
  .offer__note { top: 101px; color: var(--brand-red); font-size: 17px; font-weight: 400; }
  .offer__free { top: 138px; color: var(--brand-red); font-size: 39px; font-weight: 700; letter-spacing: -0.3px; }

  .contact { position: absolute; left: 52px; color: var(--ink-gray); font-size: 17px; line-height: 21.5px; }
  .contact--address { top: 208px; }
  .contact--phone { top: 294px; }
  .contact--web { top: 316px; }
  .contact__icon { position: absolute; left: -22px; top: 3px; width: 15px; height: 15px; fill: var(--ink-gray); }

  .pitch { position: absolute; left: 0; width: 648px; text-align: center; color: #fff; font-weight: 700; line-height: 1; padding-left: 40px; }
  .pitch--headline { top: 120px; font-size: 43px; }
  .pitch--headline span { display: block; margin-bottom: 8px; }
  .pitch--offer { top: 264px; font-size: 34px; }
  .pitch--offer span { display: block; margin-bottom: 7px; }
</style>
</head>
<body>

<section class="card card--front" aria-label="Business card front">
  <svg class="card__swoosh" viewBox="0 0 1043 595" preserveAspectRatio="none" aria-hidden="true">
    <path d="M452,595 Q700,360 1043,349 L1043,415 Q740,430 460,595 Z" fill="var(--brand-red)"/>
    <path d="M530,595 Q760,440 1043,415 L1043,595 Z" fill="var(--brand-green)"/>
  </svg>

  <div class="brand-name">
    <span class="brand-name__main">Ledgerline</span>
    <span class="brand-name__sub">Financial Group</span>
  </div>

  <div class="offer offer__amount"><span>UP TO $6,000</span><span>SAME DAY ADVANCE</span></div>
  <div class="offer offer__note">ON APPROVED TAX RETURNS!</div>
  <div class="offer offer__free">FREE ESTIMATES!</div>

  <div class="contact contact--address">
    <svg class="contact__icon" viewBox="0 0 24 24"><path d="M12 2a7 7 0 0 0-7 7c0 5 7 13 7 13s7-8 7-13a7 7 0 0 0-7-7zm0 9.5A2.5 2.5 0 1 1 12 6.5a2.5 2.5 0 0 1 0 5z"/></svg>
    Address Line Goes Here<br>Address Line Goes Here<br>Address Line Goes Here
  </div>
  <div class="contact contact--phone">
    <svg class="contact__icon" viewBox="0 0 24 24"><path d="M6.6 10.8a15 15 0 0 0 6.6 6.6l2.2-2.2a1 1 0 0 1 1-.25 11.4 11.4 0 0 0 3.6.57 1 1 0 0 1 1 1V20a1 1 0 0 1-1 1A17 17 0 0 1 3 4a1 1 0 0 1 1-1h3.5a1 1 0 0 1 1 1c0 1.25.2 2.45.57 3.57a1 1 0 0 1-.25 1z"/></svg>
    (555) 555-5555
  </div>
  <div class="contact contact--web">
    <svg class="contact__icon" viewBox="0 0 24 24"><path d="M12 2a10 10 0 1 0 0 20 10 10 0 0 0 0-20zm6.9 6h-2.9a15.6 15.6 0 0 0-1.4-3.6A8 8 0 0 1 18.9 8zM12 4a14 14 0 0 1 1.9 4h-3.8A14 14 0 0 1 12 4zM4.3 14a8 8 0 0 1 0-4h3.4a16 16 0 0 0 0 4zm.8 2h2.9a15.6 15.6 0 0 0 1.4 3.6A8 8 0 0 1 5.1 16zM8 8H5.1a8 8 0 0 1 4.3-3.6A15.6 15.6 0 0 0 8 8zm4 12a14 14 0 0 1-1.9-4h3.8A14 14 0 0 1 12 20zm2.3-6H9.7a14.7 14.7 0 0 1 0-4h4.6a14.7 14.7 0 0 1 0 4zm.3 5.6a15.6 15.6 0 0 0 1.4-3.6h2.9a8 8 0 0 1-4.3 3.6zM16.3 14a16 16 0 0 0 0-4h3.4a8 8 0 0 1 0 4z"/></svg>
    www.ledgerline.com
  </div>
</section>

<section class="card card--back" aria-label="Business card back">
  <svg class="card__swoosh" viewBox="0 0 1043 595" preserveAspectRatio="none" aria-hidden="true">
    <path d="M0,0 L530,0 Q250,80 0,312 Z" fill="var(--brand-red)"/>
    <path d="M0,312 Q420,45 1043,55 L1043,595 L0,595 Z" fill="var(--brand-green)"/>
  </svg>
  <div class="pitch pitch--headline"><span>FILE YOUR</span><span>TAXES HERE</span></div>
  <div class="pitch pitch--offer"><span>UP TO $6,000</span><span>SAME DAY ADVANCE</span></div>
</section>

</body>
</html>
```